Cover for nonfiction/memoir book "The Hidden Weather Within"

Revisions only please.

We're looking for a *nonfiction* *memoir* look that is consistent with other covers in that genre.

MUST HAVE:
- It must include the BACK COVER as it will be for print as well as an ebook.
- Title: The Hidden Weather Within
- TITLE MUST BE EASILY READ AT BRINDLECART THUMBNAIL SIZE
- Author name: Dorothea Quill
- At least one of the attached photos of Dorothea
- In COLOR
- The synopsis below
- Space for an endorsement

From the author: "I am looking for a cover that is eye catching and interesting or artistic, rather than just glamorous or pretty. If you like to edit the photos please do not completely remove the wrinkle between my eyebrows as I mention this in the book. It is okay if i look non conventional and my inner Aspie shows a little. The book is a little bit girly, and it would be good for the cover to reflect that, but mildly. No bright pink and purple designs. Please feel free to zoom in or crop the photos as you think works best"

SYNOPSIS (needs to go on the back cover)

The Hidden Weather Within is an acutely honest and often highly entertaining memoir by Dorothea Quill about life with Asperger's Syndrome. The book follows Dorothea in exploring her past and takes the reader with her on her journey to receiving and accepting her diagnosis. Instead of rehashing widely available Asperger's information, Dorothea focuses on discussing the thoughts, feelings and ideas that go along with being an Aspie, giving us a rare peek into what it really feels like to be a person on the spectrum. A must read for all those who enjoy deep personal stories or have a loved one on the spectrum that they wish to understand better.

The book dimensions will be 5x8 trade paperback and 6x9 hardcover (plus 0.25 bleed margin on all sizes - for both sizes).
Here is some more information from the publisher on cover requirements:

"I've attached a sample of both a paperback and hardcover size. Note that the spine width will be different depending on the final length of the book, so it won't be exact. That said, the front and back covers, and the flaps (for the hardcover) will always be the same as shown.
For deliverables, we need the following:

a Creative Suite 6 or earlier native .PSD (Photoshop), .ID (InDesign), or .AI (Illustrator) file. Creative Cloud files cannot be used and will not be accepted.
final file must include layered objects, and cannot be one 'background' image
Final files must be in CMYK color mode, 300dpi minimum
Total Ink saturation must be no more than 240% on any part of the cover. "True" black should use the following CMYK values: 60/40/40/100.
Fonts used in creation of the cover must be either A) embedded or B) sent with the final file
Vector art is preferred for scaling purposes"

Target Market(s)

Women of all ages. People who like psychology and personal stories.
Also parents and family members who may have a loved one on the Autism spectrum.

Requirements
Nice to have
• Bright green new leaves and greenery are good but not necessary.

```html
<!DOCTYPE html>
<html lang="en">
<head>
<meta charset="utf-8">
<title>The Hidden Weather Within — Print Cover</title>
<link rel="stylesheet" href="https://fonts.googleapis.com/css2?family=Sansita+Swashed:wght@700&family=Arimo:wght@400;700&family=EB+Garamond:ital,wght@1,700&display=swap">
<style>
  :root {
    --violet: #5b0dfb;
    --violet-deep: #3d08b8;
    --violet-band: rgba(110, 60, 220, 0.78);
    --lavender-line: #c6b2ff;
    --lavender-text: #cdbdff;
    --white: #ffffff;
    --page: #ffffff;
    --sky-lilac: #b9a6e6;
    --field-green: #79c13a;
    --grass-deep: #3f8a1f;
  }
  * { margin: 0; padding: 0; box-sizing: border-box; }
  html, body { width: 1200px; height: 1000px; overflow: hidden; background: var(--page); }
  .canvas { position: relative; width: 1200px; height: 1000px; }

  .back-cover {
    position: absolute; left: 53px; top: 82px; width: 529px; height: 793px;
    background: var(--violet);
  }
  .top-rules { position: absolute; left: 0; top: 23px; width: 100%; }
  .top-rules span { display: block; background: var(--lavender-line); }
  .top-rules .rule-thin { height: 3px; }
  .top-rules .rule-thick { height: 6px; margin-top: 6px; }

  .back-title {
    position: absolute; left: 72px; top: 82px;
    font-family: "Sansita Swashed", "Cooper Black", serif; font-weight: 700;
    font-size: 50px; line-height: 66px; color: var(--white);
  }
  .back-title .indent { display: block; padding-left: 50px; }

  .synopsis { position: absolute; left: 52px; top: 244px; width: 440px; font-family: "Arimo", Arial, sans-serif; }
  .synopsis-heading { font-size: 13px; font-weight: 700; color: var(--white); letter-spacing: 0.5px; }
  .synopsis-body { margin-top: 2px; font-size: 13.4px; line-height: 26.5px; color: var(--lavender-text); }

  .author-portrait-small {
    position: absolute; left: 394px; top: 550px; width: 108px; height: 166px;
    border: 4px solid var(--violet-deep);
    background: linear-gradient(160deg, #6fae3c 0%, #c8a878 45%, #5f9a2e 100%);
  }

  .author-band-back {
    position: absolute; left: 0; top: 733px; width: 100%; height: 26px;
    border-top: 2px solid var(--lavender-line); border-bottom: 2px solid var(--lavender-line);
  }
  .author-name {
    font-family: "EB Garamond", "Monotype Corsiva", serif; font-style: italic; font-weight: 700;
    font-size: 17px; color: var(--white);
  }
  .author-band-back .author-name { position: absolute; right: 20px; top: 1px; }

  .spine {
    position: absolute; left: 582px; top: 82px; width: 36px; height: 793px;
    background: var(--violet);
    border-left: 1px solid var(--lavender-line);
  }
  .spine-text {
    position: absolute; left: 50%; white-space: nowrap; color: var(--white);
    font-family: "EB Garamond", serif; font-style: italic; font-weight: 700;
    transform: translateX(-50%) rotate(-90deg);
  }
  .spine-author { top: 168px; font-size: 15px; width: 200px; text-align: center; margin-left: 0; }
  .spine-title { top: 560px; font-size: 20px; width: 240px; text-align: center; }

  .front-cover {
    position: absolute; left: 618px; top: 82px; width: 529px; height: 793px;
    background: var(--violet); overflow: hidden;
  }
  .front-photo {
    position: absolute; left: 0; top: 22px; width: 100%; height: 771px;
    background: linear-gradient(180deg, #a995d8 0%, var(--sky-lilac) 38%, #9fc46a 44%, var(--field-green) 60%, var(--grass-deep) 100%);
  }
  .front-rules { position: absolute; left: 0; top: 23px; width: 100%; }
  .front-rules span { display: block; background: var(--lavender-line); opacity: 0.8; }
  .front-rules .rule-thin { height: 3px; }
  .front-rules .rule-thick { height: 4px; margin-top: 5px; }

  .front-title {
    position: absolute; left: 36px; top: 272px;
    font-family: "Sansita Swashed", "Cooper Black", serif; font-weight: 700;
    font-size: 66px; line-height: 82px; color: var(--violet);
    -webkit-text-stroke: 2px var(--white); paint-order: stroke fill;
    text-shadow: 0 0 0 var(--white), 2px 2px 0 var(--white), -2px -2px 0 var(--white), 2px -2px 0 var(--white), -2px 2px 0 var(--white);
  }
  .front-title span { display: block; }

  .author-band-front {
    position: absolute; left: 0; top: 734px; width: 100%; height: 24px;
    background: var(--violet-band);
  }
  .author-band-front .author-name { position: absolute; right: 20px; top: 0; }
</style>
</head>
<body>
<main class="canvas">

  <section class="back-cover">
    <div class="top-rules"><span class="rule-thin"></span><span class="rule-thick"></span></div>
    <h2 class="back-title">The Hidden<span class="indent">Weather Within</span></h2>
    <div class="synopsis">
      <h3 class="synopsis-heading">SYNOPSIS:</h3>
      <p class="synopsis-body">The Hidden Weather Within is an acutely honest and often highly entertaining memoir by Dorothea Quill about life with Asperger's Syndrome. The book follows Dorothea in exploring her past and takes the reader with her on her journey to receiving and accepting her diagnosis. Instead of rehashing widely available Asperger's information, Dorothea focuses on discussing the thoughts, feelings and ideas that go along with being an Aspie, giving us a rare peek into what it really feels like to be a person on the spectrum. A must read for all those who enjoy deep personal stories or have a loved one on the spectrum that they wish to understand better.</p>
    </div>
    <div class="author-portrait-small" role="img" aria-label="Small photo of the author lying in green grass, writing in a notebook"></div>
    <div class="author-band-back"><span class="author-name">Author name: Dorothea Quill</span></div>
  </section>

  <section class="spine">
    <span class="spine-text spine-author">Author name: Dorothea Quill</span>
    <span class="spine-text spine-title">The Hidden Weather Within</span>
  </section>

  <section class="front-cover">
    <div class="front-photo" role="img" aria-label="Lilac-toned close-up portrait of the author above a photo of her reclining in a sunny green field in a floral dress, pen and notebook in hand"></div>
    <div class="front-rules"><span class="rule-thin"></span><span class="rule-thick"></span></div>
    <h1 class="front-title"><span>The Hidden</span><span>Weather</span><span>Within</span></h1>
    <div class="author-band-front"><span class="author-name">Author name: Dorothea Quill</span></div>
  </section>

</main>
</body>
</html>
```